Website for our 3rd party logistics warehouse company

Our company is a 3rd party logistics company. We receive and ship other businesses products for them. We offer our services to other smaller businesses that do not have a warehouse to operate out of. We also help many Brindlemart businesses prepare their products to be sold on Brindlemart.

We are looking for a modern looking design for our website. Please see our attached logo for design ideas. We are open to changing logo colors for website.

We really like the look of the website www.quorvela.com

Target Market(s)

Other businesses and brands of products

Industry/Entity Type

Warehousing and shipping

Number of Pages Required

2 page

Requirements
Must have
• We need 2 pages. Our main landing page and a duplicate page with different information geared towards brands.
Nice to have
• I like the look of overlay/transparent sections. Please see quorvela.com there is a ribbon that shows "Partners".

```html
<!DOCTYPE html>
<html lang="en">
<head>
<meta charset="utf-8">
<title>Orbitline 3PL</title>
<link rel="stylesheet" href="https://fonts.googleapis.com/css2?family=Jost:ital,wght@0,400;0,500;0,600;1,400&display=swap">
<style>
:root{
  --ink:#111;
  --amber:#f7a90d;
  --sun:#f9c85c;
  --hero-a:#f3c34f;
  --hero-b:#eaa92a;
  --card:#e2e2e2;
  --white:#fff;
}
*{box-sizing:border-box;margin:0;padding:0}
html,body{width:1200px;height:1081px;overflow:hidden;background:var(--white)}
body{position:relative;font-family:"Jost",sans-serif;color:var(--ink)}
.page{position:absolute;top:35px;width:514px;overflow:hidden}
.page--home{left:41px;height:1008px}
.page--brands{left:642px;height:782px}
.brand{position:absolute;display:flex;align-items:center;gap:4px;font-weight:600;font-size:9px;color:var(--ink);white-space:nowrap}
.brand__mark{width:8px;height:8px;background:var(--ink)}
.menu{position:absolute;right:24px;top:12px;width:19px}
.menu span{display:block;height:3px;background:var(--ink);margin-bottom:3.5px}
/* hero */
.hero{position:absolute;left:0;top:0;width:514px;height:191px;background:linear-gradient(100deg,var(--hero-a),var(--hero-b))}
.hero__texture{position:absolute;right:100px;top:0;width:130px;height:191px;background:linear-gradient(180deg,rgba(255,230,150,.35),rgba(230,150,40,.25))}
.index{position:absolute;font-size:12px;display:flex;align-items:center;gap:3px;white-space:nowrap}
.index__rule{display:inline-block;height:1px;background:var(--ink)}
.index__note{font-size:10px;margin-left:6px}
.hero h1{position:absolute;left:23px;top:96px;font-size:24px;font-weight:600}
.hero p{position:absolute;left:26px;top:150px;width:270px;font-size:10px;line-height:12px}
/* cards */
.card{position:absolute;top:191px;height:245px;background:var(--card);text-align:center}
.card--why{left:0;width:256px;box-shadow:1px 0 0 #cfcfcf}
.card--benefits{left:256px;width:258px}
.card__art{position:absolute;top:18px}
.card h2{position:absolute;left:0;right:0;top:88px;font-size:22px;font-weight:400}
.card ul{position:absolute;left:14px;right:10px;top:128px;list-style:none;font-size:10px;line-height:13.6px}
/* software */
.software{position:absolute;left:0;top:436px;width:514px;height:199px;background:var(--amber)}
.software h2{position:absolute;left:29px;top:36px;font-size:23px;font-weight:400}
.software p{position:absolute;left:30px;top:76px;width:244px;font-size:10px;line-height:12px}
.button{position:absolute;left:29px;top:143px;width:106px;height:29px;border:1px solid var(--ink);font-size:15px;line-height:27px;text-align:center}
.software__device{position:absolute;left:330px;top:22px;width:140px;height:155px;background:linear-gradient(135deg,#e9eef3,#b9c4d4 60%,#e8a11a);border-radius:10px;transform:rotate(-8deg)}
/* guarantee */
.guarantee{position:absolute;left:0;top:635px;width:514px;height:257px;background:var(--card)}
.guarantee__art{position:absolute;left:54px;top:10px;width:180px;height:171px;background:linear-gradient(135deg,#f9d21c,#f07b1c);border-radius:10px}
.guarantee h2{position:absolute;right:43px;top:22px;font-size:23px;font-weight:400}
.guarantee p.lead{position:absolute;right:36px;top:62px;width:210px;text-align:right;font-size:10.5px;line-height:13.6px}
.guarantee .form-slot{position:absolute;right:40px;top:176px;font-size:16px}
.guarantee .fine{position:absolute;left:36px;right:36px;top:200px;text-align:right;font-style:italic;font-size:5.6px;line-height:7.8px}
/* footer */
.footer{position:absolute;left:0;width:514px;background:var(--amber)}
.footer__rule{position:absolute;left:22px;width:464px;height:1px;background:#6b4a00}
.footer__nav{position:absolute;left:22px;font-size:10.5px;list-style:none}
.footer__nav li{position:absolute;white-space:nowrap}
.news__label{position:absolute;left:22px;font-size:3.6px;white-space:nowrap}
.news__input{position:absolute;left:22px;width:67px;height:8px;background:#f3f3f3;font-size:3.6px;color:#999;padding:2px 4px}
.news__button{position:absolute;left:89px;width:21px;height:8px;background:var(--ink);color:var(--white);font-size:3.6px;text-align:center;line-height:8px}
/* brands page */
.topbar{position:absolute;left:0;top:0;width:514px;height:52px;background:var(--sun)}
.intro h1{position:absolute;left:0;right:0;top:66px;text-align:center;font-size:24px;line-height:30px;font-weight:600}
.intro p{position:absolute;left:36px;right:28px;text-align:center;font-size:10px;line-height:12px}
.feature{position:absolute;top:261px;width:160px;text-align:center}
.feature__box{height:123px;background:var(--card);margin:0 2px;position:relative}
.feature__plus{position:absolute;left:50%;top:31px;width:51px;height:51px;margin-left:-25px;border-radius:50%;background:var(--white)}
.feature h3{margin-top:14px;font-size:17px;font-weight:600;line-height:21px}
.feature p{margin:9px auto 0;width:142px;font-size:10px;line-height:12px}
</style>
</head>
<body>

<section class="page page--home">
  <header class="hero">
    <div class="hero__texture" role="img" aria-label="Faint code and network texture"></div>
    <div class="brand" style="left:23px;top:24px"><span class="brand__mark"></span>Orbitline 3PL</div>
    <div class="menu"><span></span><span></span><span></span></div>
    <div class="index" style="left:21px;top:73px">01<span class="index__rule" style="width:134px"></span><span class="index__note">www.orbitline3pl.com</span></div>
    <h1>Who we are:</h1>
    <p>Orbitline 3PL is your one stop 3PL that will help you grow your business and allow you to be hands off. We offer high end services and meet our commitment, guaranteed.</p>
  </header>

  <article class="card card--why">
    <div class="card__art" role="img" aria-label="Easy to use thumbs-up illustration" style="left:104px;width:47px;height:69px;background:linear-gradient(180deg,#f4a48a,#3fc88a 55%,#b77ae0)"></div>
    <h2>Why use a prep 3PL?</h2>
    <ul>
      <li>- Work from anywhere in the world.</li>
      <li>- Don’t have to manage employees, health insurance plans, payroll, sick calls, etc.</li>
      <li>- Don’t get locked into a 3-5 year warehouse lease where you guarantee hundreds of thousands of dollars</li>
      <li>- Grow your business without commitment</li>
    </ul>
  </article>

  <article class="card card--benefits">
    <div class="card__art" role="img" aria-label="Growing coins and savings jar illustration" style="left:106px;width:66px;height:64px;background:linear-gradient(135deg,#7fc46a,#f3c21c 55%,#ef5a45)"></div>
    <h2>Benefits:</h2>
    <ul>
      <li>- 48 hour turn around guarantee – done in 48 hours or its free*</li>
      <li>- No monthly subscription – only pay for what you use</li>
      <li>- No receiving fees</li>
      <li>- No pallet or outbound fees</li>
      <li>- Email and phone support</li>
    </ul>
  </article>

  <section class="software">
    <div class="index" style="left:30px;top:16px">02<span class="index__rule" style="width:134px"></span><span class="index__note">Lorem ipsum dolor sit amet</span></div>
    <h2>Our software</h2>
    <p>Know what inventory is at our warehouse in real time. Our software allows you to track your inventory and know how your shipment status in real time. Professional software designed specifically for our needs.</p>
    <div class="button">Learn More</div>
    <div class="software__device" role="img" aria-label="Tablet showing an online store"></div>
  </section>

  <section class="guarantee">
    <div class="guarantee__art" role="img" aria-label="Certificate scroll with approval seal illustration"></div>
    <h2>Our Guarantee:</h2>
    <p class="lead">All orders will be prepped and ready for shipment in 48 business hours (often 24 or less) and we guarantee it. We are confident in our services and if we do not fulfill our obligation, we offer a 500 item (up to $700) credit on your next shipment.</p>
    <div class="form-slot">Insert Contact Form</div>
    <p class="fine">*Our guarantee is 48 hours from the time an outbound shipment is created in our system. Weekends and holidays excluded. Orders created on a Friday after hours, Saturday or Sunday will be counted from the open of business on Monday morning. We offer a credit of up to 500 units on your next shipment. These credits are for standard prep items only, no bundles, bubble wrapped or multipack units. Outbound shipments will be prepped and ready to ship. We are unable to control shipping companies and freight carriers. Orders after daily pickups are completed will be ready for next day pickup.</p>
  </section>

  <footer class="footer" style="top:892px;height:116px">
    <div class="brand" style="left:22px;top:22px"><span class="brand__mark"></span>Orbitline 3PL</div>
    <div class="footer__rule" style="top:53px"></div>
    <ul class="footer__nav" style="top:57px">
      <li style="left:0">HOME</li><li style="left:116px">GROW</li><li style="left:225px">DISTRIBUTE</li><li style="left:344px">CONTACT</li>
    </ul>
    <div class="news__label" style="top:79px">Stay up to date with our newsletter</div>
    <div class="news__input" style="top:86px">Email Address</div>
    <div class="news__button" style="top:86px">Sign Up!</div>
  </footer>
</section>

<section class="page page--brands">
  <header class="topbar">
    <div class="brand" style="left:26px;top:21px"><span class="brand__mark"></span>Orbitline 3PL</div>
    <div class="menu"><span></span><span></span><span></span></div>
  </header>

  <div class="intro">
    <h1>Why Direct to Consumer?</h1>
    <p style="top:108px">Direct to Consumer (D2C) is rapidly growing due to consumer confidence. D2C allows for increased manufacturer profits, often allowing for profit margins grow 2-5X over wholesale profits. D2C sales allow for long-term customer relationships while decreasing customer acquisition costs. D2C allows for subscription-based services, allowing for customer ease of repurchasing products without investing time or thought. Increase customer lifetime value without increasing marketing costs.</p>
    <p style="top:187px">Brands often worry about current supply chain and distribution of their products to distributors and wholesalers. D2C allows for more consumer purchasing options while preserving current purchasing channels such as third party online stores and retail stores. D2C allows for successful symbiotic relationship with other retailers while maintaining price integrity.</p>
  </div>

  <article class="feature" style="left:14px">
    <div class="feature__box"><div class="feature__plus"><svg width="51" height="51" viewBox="0 0 51 51"><path d="M25.5 14v23M14 25.5h23" stroke="#111" stroke-width="3.5"/></svg></div></div>
    <h3>Logistics</h3>
    <p style="margin-top:21px">We take care of all the logistics and keeping you in stock at Brindlemart. Simply send your inventory to us and we do the rest. We can reduce your labor costs and grow help grow your company at the same time. Your dedicated account manager will stay in contact when its time to ship stock to our warehouse.</p>
  </article>

  <article class="feature" style="left:178px">
    <div class="feature__box"><div class="feature__plus"><svg width="51" height="51" viewBox="0 0 51 51"><path d="M25.5 14v23M14 25.5h23" stroke="#111" stroke-width="3.5"/></svg></div></div>
    <h3>Take control of<br>your brand</h3>
    <p>Improve your customer experience and your brand’s value by selling direct to consumer. Direct to consumer offers higher customer confidence as well as increased profits. Don’t allow companies to lower your product value by racing the price to the bottom or have to police companies breaking MAP pricing. Focus on your advertising, R&amp;D, and brand growth. Don’t waste time and labor on learning the Brindlemart logistics process. We also expanding to Halvorn HFS, Listmoor and Cartwell.</p>
  </article>

  <article class="feature" style="left:342px">
    <div class="feature__box"><div class="feature__plus"><svg width="51" height="51" viewBox="0 0 51 51"><path d="M25.5 14v23M14 25.5h23" stroke="#111" stroke-width="3.5"/></svg></div></div>
    <h3>Our Guarantee:</h3>
    <p style="margin-top:21px">We guarantee that our services will increase your account sales and profits, even after our service costs. If you do not see an increase in gross revenues within 3 months, we won’t charge you a thing.</p>
  </article>

  <footer class="footer" style="top:664px;height:118px">
    <div class="brand" style="left:22px;top:24px"><span class="brand__mark"></span>Orbitline 3PL</div>
    <div class="footer__rule" style="top:54px"></div>
    <ul class="footer__nav" style="top:59px">
      <li style="left:0">HOME</li><li style="left:116px">GROW</li><li style="left:226px">DISTRIBUTE</li><li style="left:345px">CONTACT</li>
    </ul>
    <div class="news__label" style="top:81px">Stay up to date with our newsletter</div>
    <div class="news__input" style="top:88px">Email Address</div>
    <div class="news__button" style="top:88px">Sign Up!</div>
  </footer>
</section>

</body>
</html>
```